Design a Professional Business Card for Velmora Arcs

Design a business card for Velmora Arcs, we are a National Sport Court Company.

West Region Address: 4175 Quill Harbor Ln, Suite #215 Ashcombe, Colorado 80467
East Region Address: 3817 Tamsin Rd E, Marlowe Bay, Florida 34583

Target Market(s)

High End Residential & Institutional Clients

Industry/Entity Type

Design & Construction

Contact Information for Business Card

Logo/Brand/Colors/ name, number (provided in comments)

Requirements
Must have
• Colors only provided in logo
Should not have
• Any other colors not in existing logo (attached)

```html
<!DOCTYPE html>
<html lang="en">
<head>
<meta charset="utf-8">
<title>Velmora Arcs — Business Card</title>
<link rel="stylesheet" href="https://fonts.googleapis.com/css2?family=Roboto:wght@400;500;700;900&display=swap">
<style>
  :root {
    --navy: #1b3467;
    --green: #116b39;
    --white: #ffffff;
    --ink: #3a3a3a;
    --rule: #c9c9c9;
    --ghost: #f2f4f4;
    --backdrop: #e4e4e4;
  }
  html, body {
    margin: 0;
    width: 1200px;
    height: 1200px;
    overflow: hidden;
    background: var(--backdrop);
    font-family: "Roboto", Arial, sans-serif;
  }
  .canvas { position: relative; width: 1200px; height: 1200px; }
  .card {
    position: absolute;
    left: 264px;
    width: 690px;
    height: 394px;
    overflow: hidden;
    box-shadow: 0 2px 3px rgba(0,0,0,0.12);
  }
  .card--front { top: 158px; background: var(--white); }
  .card--back { top: 653px; background: var(--green); }

  .ghost-circle {
    position: absolute;
    left: -110px; top: 0;
    width: 450px; height: 450px;
    border-radius: 50%;
    background: var(--ghost);
  }

  .brand { position: absolute; display: flex; align-items: center; }
  .brand__dot { border-radius: 50%; flex: none; }
  .brand__name {
    font-weight: 900;
    text-transform: uppercase;
    line-height: 0.98;
  }
  .card--front .brand { left: 308px; top: 47px; gap: 16px; }
  .card--front .brand__dot { width: 88px; height: 88px; background: var(--navy); }
  .card--front .brand__name { font-size: 37px; color: var(--navy); letter-spacing: 0.11em; }
  .card--back .brand { left: 134px; top: 138px; gap: 26px; }
  .card--back .brand__dot { width: 117px; height: 117px; background: var(--white); }
  .card--back .brand__name { font-size: 48px; color: var(--white); letter-spacing: 0.13em; }

  .person { position: absolute; left: 48px; top: 221px; }
  .person__name { margin: 0; font-size: 28px; font-weight: 700; color: var(--navy); letter-spacing: 0.01em; }
  .person__title { margin: 2px 0 0; font-size: 16px; color: var(--green); }

  .contact { position: absolute; right: 44px; top: 226px; list-style: none; margin: 0; padding: 0; text-align: right; }
  .contact li { display: flex; align-items: center; justify-content: flex-end; gap: 10px; font-size: 16px; color: var(--ink); line-height: 21px; }
  .contact svg { width: 14px; height: 14px; fill: var(--navy); }

  .divider { position: absolute; left: 48px; right: 44px; top: 281px; height: 1px; background: var(--rule); }

  .addresses { position: absolute; left: 42px; width: 616px; top: 291px; text-align: center; font-size: 16px; line-height: 21px; color: var(--ink); margin: 0; font-style: normal; }

  .band { position: absolute; left: 0; bottom: 0; width: 690px; height: 36px; }
  .band__web { position: absolute; right: 41px; bottom: 6px; font-size: 16px; color: var(--white); }
</style>
</head>
<body>
<div class="canvas">

  <section class="card card--front">
    <div class="ghost-circle"></div>

    <div class="brand">
      <span class="brand__dot"></span>
      <span class="brand__name">Velmora<br>Arcs</span>
    </div>

    <div class="person">
      <h1 class="person__name">DALE HARMON</h1>
      <p class="person__title">President</p>
    </div>

    <ul class="contact">
      <li>412-555-0193
        <svg viewBox="0 0 24 24" aria-hidden="true"><path d="M6.6 10.8a15.5 15.5 0 0 0 6.6 6.6l2.2-2.2c.3-.3.7-.4 1-.2 1.1.4 2.3.6 3.6.6.6 0 1 .4 1 1V20c0 .6-.4 1-1 1A17 17 0 0 1 3 4c0-.6.4-1 1-1h3.5c.6 0 1 .4 1 1 0 1.3.2 2.5.6 3.6.1.3 0 .7-.2 1z"/></svg>
      </li>
      <li>info@velmoraarcs.com
        <svg viewBox="0 0 24 24" aria-hidden="true"><path d="M2 5h20v14H2zM4 7v.5l8 5 8-5V7zm0 2.8V17h16V9.8l-8 5z"/></svg>
      </li>
    </ul>

    <div class="divider"></div>

    <address class="addresses">
      West Region: 4175 Quill Harbor Ln, Suite #215 Ashcombe, Colorado 80467<br>
      East Region: 3817 Tamsin Rd E, Marlowe Bay, Florida 34583
    </address>

    <svg class="band" viewBox="0 0 690 36" preserveAspectRatio="none" aria-hidden="true">
      <rect x="0" y="21" width="430" height="15" fill="var(--green)"/>
      <polygon points="418,36 445,3 690,3 690,36" fill="var(--white)"/>
      <polygon points="422,36 448,2 690,2 690,36" fill="var(--navy)"/>
    </svg>
    <span class="band__web">www.velmoraarcs.com</span>
  </section>

  <section class="card card--back">
    <div class="brand">
      <span class="brand__dot"></span>
      <span class="brand__name">Velmora<br>Arcs</span>
    </div>
  </section>

</div>
</body>
</html>
```